Harrowgate Building and Property Services needs a business card design

We need a business card design for our building and property services business. We already have a logo we just need a creative design and layout on a business card. Emphasis on clean, modern, professional.
Our client targets are mainly body corporates, building managers, construction managers.
We are a building services company that lean more to structural repair of buildings, through concrete rectification and carbon fibre strengthening.
We also refurbish facades, rendering, painting etc
We target higher end body corporates in prestigious locations, hence why we'd like our cards to reflect professionalism, strength, efficiency

Target Market(s)

body corporates, building managers, construction managers

Industry/Entity Type

Construction

Contact Information for Business Card

Harrowgate is the main word, with 'Building and Property Services' underneath.
Level 17, 88 Marsh Lane
ELMSWORTH
Melbourne
Vic 3942
T: 9218 5371
Duncan Hensley - Director
dunharrowgate@mailbox-example.net

Requirements
Must have
• Stand out on the back of the card- strong/ bold, company logo
• All of the contact details written above
Should not have
• I'd like the card to stand out, especially on the back. Id like the company logo to be prominent, although feel free to be creative around it. But remain clean and professional

```html
<!DOCTYPE html>
<html lang="en">
<head>
<meta charset="utf-8">
<title>Harrowgate Building and Property Services – Business Card</title>
<link href="https://fonts.googleapis.com/css2?family=Cinzel:wght@400&family=Open+Sans:wght@400;700&display=swap" rel="stylesheet">
<style>
  :root {
    --stage: #ecedef;
    --blue-deep: #0a6db4;
    --blue-mid: #1b93d6;
    --blue-light: #3bb2ec;
    --blue-brand: #29a3de;
    --grey-band: #58595b;
    --ink: #2a2a2a;
    --white: #ffffff;
  }
  * { box-sizing: border-box; margin: 0; padding: 0; }
  html, body { width: 1200px; height: 800px; overflow: hidden; }
  body {
    background: var(--stage);
    font-family: "Open Sans", Arial, sans-serif;
    display: flex;
    align-items: center;
    justify-content: center;
    gap: 40px;
  }
  .card {
    position: relative;
    width: 540px;
    height: 309px;
    overflow: hidden;
    box-shadow: 0 6px 18px rgba(0,0,0,0.18);
  }

  /* Back of card */
  .card-back {
    background: linear-gradient(160deg, var(--blue-deep) 0%, var(--blue-mid) 55%, var(--blue-light) 100%);
  }
  .card-back .world-area {
    position: absolute;
    left: 40px; top: 50px;
    width: 460px; height: 210px;
    border-radius: 40%;
    background: radial-gradient(ellipse at center, rgba(255,255,255,0.12) 0%, rgba(255,255,255,0) 70%);
  }
  .card-back .brand {
    position: absolute;
    left: 0; right: 0; top: 118px;
    text-align: center;
    color: var(--white);
  }
  .brand-name {
    font-family: "Cinzel", Georgia, serif;
    font-weight: 400;
    font-size: 30px;
    letter-spacing: 4px;
    white-space: nowrap;
  }
  .brand-tag {
    font-family: "Cinzel", Georgia, serif;
    font-size: 8px;
    letter-spacing: 1.6px;
    text-transform: uppercase;
    margin-top: 2px;
    white-space: nowrap;
  }
  .brand-mark {
    display: block;
    width: 14px; height: 14px;
    margin: 0 auto 12px;
    background: currentColor;
  }

  /* Front of card */
  .card-front { background: var(--white); }
  .card-front .brand {
    position: absolute;
    left: 70px; width: 280px; top: 34px;
    color: var(--blue-brand);
    text-align: center;
  }
  .card-front .brand-name { font-size: 26px; }
  .contact-band {
    position: absolute;
    left: 270px; right: 0; top: 122px;
    height: 74px;
    background: var(--grey-band);
    color: var(--white);
    padding: 15px 0 0 22px;
    font-size: 12px;
  }
  .contact-band .notch {
    position: absolute;
    left: 0; bottom: 0;
  }
  .contact-line {
    display: flex; align-items: center; gap: 8px;
    line-height: 22px; white-space: nowrap;
  }
  .contact-line svg { flex: none; }
  .person-band {
    position: absolute;
    left: 0; top: 196px;
    width: 270px; height: 64px;
    background: linear-gradient(90deg, var(--blue-brand), var(--blue-mid));
    color: var(--white);
    padding: 10px 0 0 100px;
    white-space: nowrap;
  }
  .person-band .notch {
    position: absolute;
    left: 80px; top: 0;
  }
  .person-name {
    font-weight: 700;
    font-size: 16px;
    line-height: 24px;
    text-transform: uppercase;
    letter-spacing: 0.3px;
  }
  .person-role { font-size: 12px; line-height: 18px; margin-left: 60px; }
  .address {
    position: absolute;
    left: 0; right: 0; bottom: 18px;
    text-align: right;
    padding-right: 24px;
    font-size: 12.5px;
    color: var(--ink);
    white-space: nowrap;
  }
</style>
</head>
<body>

  <section class="card card-back" aria-label="Business card, back">
    <div class="world-area" role="img" aria-label="Faint dotted world map behind the company name"></div>
    <div class="brand">
      <span class="brand-mark" aria-hidden="true"></span>
      <div class="brand-name">HARROWGATE</div>
      <div class="brand-tag">Building and Property Services</div>
    </div>
  </section>

  <section class="card card-front" aria-label="Business card, front">
    <div class="brand">
      <span class="brand-mark" aria-hidden="true"></span>
      <div class="brand-name">HARROWGATE</div>
      <div class="brand-tag">Building and Property Services</div>
    </div>

    <div class="contact-band">
      <svg class="notch" width="16" height="10" viewBox="0 0 16 10" aria-hidden="true">
        <polygon points="0,10 16,10 8,0" fill="var(--blue-brand)"/>
      </svg>
      <div class="contact-line">
        <svg width="13" height="13" viewBox="0 0 13 13" aria-hidden="true">
          <circle cx="6.5" cy="6.5" r="6.5" fill="var(--blue-brand)"/>
          <path d="M4 3.5h1.5l.7 1.8-.9.6a5 5 0 0 0 2.3 2.3l.6-.9 1.8.7V9.5a1 1 0 0 1-1 1A6 6 0 0 1 3 4.5a1 1 0 0 1 1-1z" fill="var(--white)"/>
        </svg>
        <span>9218 5371</span>
      </div>
      <div class="contact-line">
        <svg width="13" height="13" viewBox="0 0 13 13" aria-hidden="true">
          <circle cx="6.5" cy="6.5" r="6.5" fill="var(--blue-brand)"/>
          <rect x="3.3" y="4.2" width="6.4" height="4.6" fill="none" stroke="var(--white)" stroke-width="0.9"/>
          <polyline points="3.3,4.2 6.5,6.8 9.7,4.2" fill="none" stroke="var(--white)" stroke-width="0.9"/>
        </svg>
        <span>dunharrowgate@mailbox-example.net</span>
      </div>
    </div>

    <div class="person-band">
      <svg class="notch" width="18" height="10" viewBox="0 0 18 10" aria-hidden="true">
        <polygon points="0,0 18,0 9,10" fill="var(--white)"/>
      </svg>
      <div class="person-name">Duncan Hensley</div>
      <div class="person-role">Director</div>
    </div>

    <div class="address">Level 17, 88 Marsh Lane, ELMSWORTH, Melbourne Vic 3942</div>
  </section>

</body>
</html>
```